Basisdesign Buch-/E-Book-Cover für Lindqvist-Krimis
Sehr gute Zusammenarbeit! Soraya setzt sich ernsthaft mit dem Briefing auseinander, reagiert prompt und konstruktiv auf Änderungswünsche, kommuniziert kompetent und hilfsbereit. Äußerst empfehlenswert.
Zielgruppe
Ich schreibe Krimis, Thriller, Kriminalstories, Krimiparodien.
Meine Zielgruppe sind deutschsprachige Krimi-Leser.
Aufgabenstellung
Ich benötige ein Basisdesign für Buchcover (Höhe 2.343, Breite 1.518 Pixel – Print Forge, eBooks). Alle Bücher haben mit Crime zu tun, aber in verschiedenen Unter-Genres: Klassischer Kriminalroman, Thriller, Fantasy Thriller, Kurzgeschichten, Krimi-Parodien.
Ich benötige, quasi als Marke, dafür ein gleichbleibendes grafisches Element, z. B. einen Sockel im unteren Coverbereich, der den Autorennamen „Tobias Lindqvist“ und das jeweilige Unter-Genre enthält. Unter-Genres sind: Krimi, Thriller, Fantasy-Thriller, Kurzgeschichten und Krimi-Parodie. Das alles sollte auch noch im Format der Bücherhafen-Bücherlisten wie „Kunden kauften auch“ halbwegs lesbar sein.
Ein bisschen mörderisch und blutig sind alle Varianten.
Nachdem die Bandbreite vom Thriller bis zur Parodie reicht, sollte der gleichbleibende Markenbereich eine entsprechende grafische Bandbreite aufweisen, dabei aber die Grundmelodie Crime nicht aus den Augen verlieren.
Im oberen Bereich stelle ich mir Grafiken oder Hintergrundfotos vor, die für jedes Buch individuell gestaltet werden müssten, was jedoch über das Basisdesign hinausgeht. Die Wahl der Schriftart für Titel (bislang 11 – 25 Zeichen inkl. Leerzeichen) und allfällige Untertitel (im Umfang von maximal 30 Zeichen), sollte zu denen im Sockel passen.

```html
<!DOCTYPE html>
<html lang="de">
<head>
<meta charset="utf-8">
<title>Lindqvist-Krimis – Basisdesign Buchcover</title>
<link rel="stylesheet" href="https://fonts.googleapis.com/css2?family=Bebas+Neue&family=Open+Sans:wght@600;700&family=Tinos&display=swap">
<style>
  :root {
    --page-bg: #ffffff;
    --cover-dark: #252b2e;
    --mist-light: #b3afa5;
    --mist-mid: #7d817c;
    --blood-red: #c0312f;
    --badge-red: #a51c1e;
    --badge-ink: #1d1d1d;
    --name-cream: #f4f0d8;
  }
  * { margin: 0; padding: 0; box-sizing: border-box; }
  html, body {
    width: 1200px;
    height: 848px;
    overflow: hidden;
    background: var(--page-bg);
  }
  .canvas {
    position: relative;
    width: 1200px;
    height: 848px;
  }
  .cover {
    position: absolute;
    left: 357px;
    top: 44px;
    width: 485px;
    height: 760px;
    background: var(--cover-dark);
    overflow: hidden;
  }
  .cover-photo {
    position: absolute;
    left: 0;
    top: 0;
    width: 100%;
    height: 260px;
    background:
      linear-gradient(180deg,
        #5c625e 0%,
        var(--mist-mid) 8%,
        var(--mist-light) 28%,
        #8e8d85 52%,
        #3f4645 74%,
        var(--cover-dark) 100%);
  }
  .title {
    position: absolute;
    left: 0;
    width: 100%;
    top: 95px;
    text-align: center;
    font-family: "Tinos", "Times New Roman", serif;
    font-size: 208px;
    line-height: 1;
    color: var(--blood-red);
    letter-spacing: -2px;
  }
  .badge {
    position: absolute;
    left: -15px;
    top: 465px;
    width: 152px;
    height: 152px;
    border-radius: 50%;
    background: var(--badge-red);
    box-shadow: 3px 4px 8px rgba(0,0,0,0.45);
    display: flex;
    flex-direction: column;
    align-items: center;
    justify-content: center;
    font-family: "Open Sans", Arial, sans-serif;
    font-weight: 700;
    color: var(--badge-ink);
    line-height: 1.1;
    text-align: center;
  }
  .badge-line { font-size: 17px; font-weight: 600; }
  .badge-line--strong { font-size: 25px; font-weight: 700; }
  .badge-dots { font-size: 14px; letter-spacing: 1px; }
  .author {
    position: absolute;
    left: 0;
    width: 100%;
    top: 588px;
    text-align: center;
    font-family: "Bebas Neue", "Oswald", sans-serif;
    color: var(--name-cream);
  }
  .author-first {
    display: block;
    font-size: 88px;
    line-height: 0.8;
  }
  .author-last {
    display: block;
    font-size: 102px;
    line-height: 0.8;
    margin-top: 6px;
  }
  .genre {
    position: absolute;
    right: 74px;
    top: 687px;
    font-family: "Open Sans", Arial, sans-serif;
    font-weight: 600;
    font-size: 17px;
    letter-spacing: 4px;
    color: var(--blood-red);
    line-height: 1;
  }
</style>
</head>
<body>
  <main class="canvas">
    <section class="cover">
      <div class="cover-photo" role="img" aria-label="Hintergrundfoto: Eiszapfen mit rotem Blutstropfen vor nebligem, winterlichem Himmel"></div>
      <h1 class="title">titel</h1>
      <div class="badge">
        <span class="badge-line">KUNDEN</span>
        <span class="badge-line--strong">KAUFTEN</span>
        <span class="badge-line">AUCH</span>
        <span class="badge-dots">....</span>
      </div>
      <p class="author">
        <span class="author-first">TOBIAS</span>
        <span class="author-last">LINDQVIST</span>
      </p>
      <span class="genre">KRIMI</span>
    </section>
  </main>
</body>
</html>
```